Landscaping Contract with customizable fillable form

Need a PDF Template with a format that can be filled in with info by us. Then sent to the customer for signature. form need to be able to be changed for each customer

Industry/Entity Type

Landscaping

Colors
00AB8E
00BBA5
67D7C9
C6EFE9
E9F9F6

```html
<!DOCTYPE html>
<html lang="en">
<head>
<meta charset="utf-8">
<title>Yard Work Contract</title>
<link href="https://fonts.googleapis.com/css2?family=Libre+Baskerville:wght@700&family=Montserrat:wght@400;500;600&display=swap" rel="stylesheet">
<style>
  :root{
    --backdrop:#5f6669;
    --green-deep:#2f5526;
    --green-mid:#64a34c;
    --title-green:#2e5a23;
    --band:#d8ecd6;
    --ink:#1e1e1e;
    --dot:#1f6a3a;
    --dot-light:#d6ead2;
    --paper:#ffffff;
    --grey-a:#c9c9c9;
    --grey-b:#eeeeee;
  }
  html,body{margin:0;padding:0;width:1200px;height:1200px;overflow:hidden;background:var(--backdrop);}
  .page{position:absolute;left:133px;top:0;width:1356px;height:1744px;transform:scale(.6881);transform-origin:top left;
    background:linear-gradient(90deg,var(--grey-a),var(--grey-b) 60%,var(--grey-a));font-family:"Montserrat",sans-serif;color:var(--ink);}
  .page-frame{position:absolute;left:0;top:0;}
  .sheet{position:absolute;left:37px;top:74px;width:1282px;height:1595px;background:var(--paper);
    border-radius:200px 0 260px 0;}
  .brand{position:absolute;left:0;right:0;top:126px;display:flex;flex-direction:column;align-items:center;gap:14px;}
  .brand-dot{width:54px;height:54px;border-radius:50%;background:var(--dot);}
  .brand-name{font-size:26px;font-weight:600;color:var(--dot);letter-spacing:1px;}
  .title-band{position:absolute;left:0;top:250px;width:1282px;height:64px;background:var(--band);
    display:flex;align-items:center;justify-content:center;}
  .title{margin:0;font-family:"Libre Baskerville",serif;font-weight:700;font-size:37px;color:var(--title-green);letter-spacing:.5px;}
  .intro{position:absolute;left:43px;top:355px;width:1180px;margin:0;font-size:22px;line-height:28.7px;text-align:justify;}
  .blank{display:inline-block;border-bottom:1.5px solid var(--ink);height:18px;vertical-align:baseline;}
  .terms{position:absolute;left:0;top:0;margin:0;padding:0;list-style:none;}
  .term{position:absolute;left:121px;width:1112px;font-size:22px;line-height:28.7px;text-align:justify;}
  .term-no{position:absolute;left:-32px;top:0;font-weight:600;font-size:23px;}
  .timeline{position:absolute;left:0;top:0;}
  .signatures{position:absolute;left:117px;top:0;font-size:22px;}
  .sig{position:absolute;left:0;white-space:nowrap;}
</style>
</head>
<body>
<div class="page">
  <svg class="page-frame" width="1356" height="1744" viewBox="0 0 1356 1744">
    <defs>
      <linearGradient id="frameGreen" x1="0" y1="0" x2="1" y2="0">
        <stop offset="0" stop-color="#2f5526"/>
        <stop offset=".5" stop-color="#64a34c"/>
        <stop offset="1" stop-color="#2f5526"/>
      </linearGradient>
    </defs>
    <polygon points="0,0 1356,0 1356,1010 1319,1048 37,1110 0,1083" fill="url(#frameGreen)"/>
    <rect x="0" y="80" width="1356" height="1030" fill="#2f5526" opacity=".0"/>
  </svg>

  <div class="sheet">
    <div class="brand">
      <div class="brand-dot"></div>
      <div class="brand-name">GREENHOLLOW ESTATE CARE</div>
    </div>
    <div class="title-band"><h1 class="title">YARD WORK CONTRACT</h1></div>

    <p class="intro">This contract is made between <span class="blank" style="width:366px"></span> (hereafter known as the Client) and <span class="blank" style="width:236px"></span> (hereafter known as the Contractor). The Client desires to have certain maintenance services, described below, performed upon a yard located at .<br><span class="blank" style="width:236px"></span> Therefore, the parties hereby agree as follows:</p>

    <svg class="timeline" width="140" height="1400" viewBox="0 0 140 1400">
      <line x1="58" y1="540" x2="58" y2="1190" stroke="#1e1e1e" stroke-width="2"/>
      <g stroke="#1e1e1e" stroke-width="2.5">
        <circle cx="58" cy="540" r="17" fill="#fff"/>
        <circle cx="58" cy="621" r="17" fill="#fff"/>
        <circle cx="58" cy="707" r="17" fill="#fff"/>
        <circle cx="58" cy="819" r="17" fill="#fff"/>
        <circle cx="58" cy="962" r="17" fill="#fff"/>
        <circle cx="58" cy="1076" r="17" fill="#fff"/>
        <circle cx="58" cy="1190" r="17" fill="#fff"/>
      </g>
      <g>
        <circle cx="58" cy="540" r="10" fill="var(--dot)"/>
        <circle cx="58" cy="621" r="10" fill="var(--dot-light)"/>
        <circle cx="58" cy="707" r="10" fill="var(--dot)"/>
        <circle cx="58" cy="819" r="10" fill="var(--dot-light)"/>
        <circle cx="58" cy="962" r="10" fill="var(--dot)"/>
        <circle cx="58" cy="1076" r="10" fill="var(--dot-light)"/>
        <circle cx="58" cy="1190" r="10" fill="var(--dot)"/>
      </g>
    </svg>

    <ol class="terms">
      <li class="term" style="top:524px"><span class="term-no">1.</span>Client shall grant Contractor access to the yard and its surroundings during regular business hours and other mutually agreeable times.</li>
      <li class="term" style="top:609px"><span class="term-no">2.</span>(Client or Contractor) shall provide all equipment and consumable supplies necessary to perform maintenance services on the yard.</li>
      <li class="term" style="top:694px"><span class="term-no">3.</span>Client shall pay Contractor $X on the first day of each (week or month) for regular maintenance services to be performed during the rest of that (week or month). See "Regular Maintenance" description below.</li>
      <li class="term" style="top:807px"><span class="term-no">4.</span>Client shall pay Contractor for any additional maintenance or repair work that may become necessary to maintain a pleasing, safe, and horticulturally healthy yard (hereafter known as "ad hoc work"). Contractor shall bill Client for the cost of ad hoc work and Client shall include payment with Client's next payment for regular maintenance.</li>
      <li class="term" style="top:950px"><span class="term-no">5.</span>Ad hoc work whose cost is less than $50 may be performed by Contractor without Clients explicit authorization. Work which Contractor estimates will cost $50 or more shall be authorized by Client before it is performed.</li>
      <li class="term" style="top:1063px"><span class="term-no">6.</span>"Regular Maintenance" shall include removal of debris from the yard; mowing of lawn and trimming of shrubs, trees, and other plants; fertilization and other conditioning of the yard's soil; inspection of plants and soil for pests, and extermination of any pests discovered.</li>
      <li class="term" style="top:1176px"><span class="term-no">7.</span>Contractor shall begin performing regular maintenance on MMODNYYY. Thereafter, regular maintenance shall be performed on a schedule to which the parties agree. 8. Either party may terminate this agreement with written notice to the other party. Any payment for services rendered owed by Client shall be due and payable at the time this agreement is terminated.</li>
    </ol>

    <div class="signatures">
      <div class="sig" style="top:1352px">Client's signature, date</div>
      <div class="sig" style="top:1433px">Contractor's Signature, date</div>
      <div class="sig" style="top:1514px">Client's printed name</div>
    </div>
  </div>
</div>
</body>
</html>
```